Tavlune

I'd like new business card design options. I'll need to provide updated contact info although after the deign is complete. We are in IT, specifically in the data backup, archiving and disaster recovery verticals.

Business

```html
<!DOCTYPE html>
<html lang="en">
<head>
<meta charset="utf-8">
<title>Tavlune – Business Card</title>
<link rel="stylesheet" href="https://fonts.googleapis.com/css2?family=Montserrat:wght@600;700;800&family=Open+Sans:wght@400;600&display=swap">
<style>
  :root {
    --page: #e9e6e1;
    --blue-deep: #0a5cb0;
    --blue-bright: #1b8fd8;
    --paper: #f3f3f3;
    --ink: #2b2b2b;
    --white: #ffffff;
  }
  * { margin: 0; padding: 0; box-sizing: border-box; }
  html, body { width: 1200px; height: 900px; overflow: hidden; }
  body {
    background: var(--page);
    font-family: "Open Sans", Arial, sans-serif;
    position: relative;
  }
  .card {
    position: absolute;
    left: 320px;
    width: 560px;
    height: 320px;
    overflow: hidden;
    box-shadow: 0 6px 18px rgba(0,0,0,0.18);
  }
  .card--front { top: 95px; background: var(--blue-deep); }
  .card--back { top: 475px; background: var(--paper); }

  /* front */
  .front-band {
    position: absolute; left: 0; right: 0; top: 180px; bottom: 0;
    background: var(--blue-bright);
  }
  .front-brand {
    position: absolute; left: 0; right: 0; top: 102px;
    display: flex; align-items: center; justify-content: center; gap: 18px;
  }
  .brand-dot {
    width: 56px; height: 56px; border-radius: 50%;
    background: var(--blue-bright);
    flex: none;
  }
  .brand-name {
    font-family: "Montserrat", Arial, sans-serif;
    font-weight: 800; font-size: 38px; letter-spacing: 7px;
    color: var(--white); line-height: 1;
  }
  .services {
    position: absolute; left: 0; right: 0; bottom: 56px;
    text-align: center; color: var(--white);
    font-family: "Montserrat", Arial, sans-serif;
    font-weight: 600; font-size: 15.5px;
  }

  /* back */
  .card-wave { position: absolute; left: 0; top: 0; width: 560px; height: 320px; }
  .person { position: absolute; left: 34px; top: 30px; }
  .person-name {
    font-family: "Montserrat", Arial, sans-serif;
    font-weight: 700; font-size: 20px; color: var(--blue-deep);
  }
  .person-role { font-size: 13px; color: var(--ink); margin-top: 1px; }
  .back-brand {
    position: absolute; right: 30px; top: 34px;
    display: flex; align-items: center; gap: 12px;
  }
  .back-brand .brand-dot {
    width: 40px; height: 40px; background: var(--blue-deep);
  }
  .back-brand .brand-name { color: var(--blue-deep); font-size: 24px; letter-spacing: 4px; }
  .contact { position: absolute; left: 40px; top: 104px; list-style: none; }
  .contact li {
    display: flex; align-items: center; gap: 10px;
    font-size: 13.5px; color: var(--ink); line-height: 20px;
  }
  .contact svg { width: 12px; height: 12px; fill: var(--blue-deep); flex: none; }
  .address {
    position: absolute; left: 62px; top: 190px;
    font-size: 13.5px; color: var(--ink); line-height: 20px;
  }
</style>
</head>
<body>

<section class="card card--front">
  <div class="front-band"></div>
  <div class="front-brand">
    <div class="brand-dot"></div>
    <div class="brand-name">TAVLUNE</div>
  </div>
  <p class="services">Data Backup &nbsp;|&nbsp; Archiving &nbsp;|&nbsp; Disaster Recovery Verticals</p>
</section>

<section class="card card--back">
  <svg class="card-wave" viewBox="0 0 560 320" aria-hidden="true">
    <path d="M0,250 C170,292 360,264 474,188 C390,270 190,302 0,274 Z" fill="var(--blue-bright)"/>
    <path d="M0,286 C180,318 390,282 560,140 L560,320 L0,320 Z" fill="var(--blue-deep)"/>
  </svg>

  <div class="person">
    <div class="person-name">DANIEL CARVER</div>
    <div class="person-role">Managing Director</div>
  </div>

  <div class="back-brand">
    <div class="brand-dot"></div>
    <div class="brand-name">TAVLUNE</div>
  </div>

  <ul class="contact">
    <li><svg viewBox="0 0 12 12"><path d="M1 4c0-2 2-3 5-3s5 1 5 3l-2 1-1-2H4L3 5zM3 6h6l1 5H2z"/></svg>(044)123456789</li>
    <li><svg viewBox="0 0 12 12"><path d="M3 1h6v3H3zM1 4h10v7H1zM3 6v1h2V6zm4 0v1h2V6zM3 8v1h2V8zm4 0v1h2V8z"/></svg>(044)123456789</li>
    <li><svg viewBox="0 0 12 12"><path d="M0 2h12v1L6 7 0 3zM0 4.5l6 4 6-4V10H0z"/></svg>info@youremail.com</li>
    <li><svg viewBox="0 0 12 12"><circle cx="6" cy="6" r="5.5"/></svg>www.websitename.com</li>
  </ul>
  <p class="address">1234, Address GoesHere,<br>Country name, 12345</p>
</section>

</body>
</html>
```